Linwell Psychology website transfer from WIX to Wordpress

I have a website currently coded in WIX and I want it (or something like it or better) designed to be coded on Wordpress instead. The website should have mobile optimization so that it can be viewed on mobile devices.

The current website is at: www.linwellpsychology.example

I'm not looking for versions of the website that are very different to what I already have, unless they improve on it aesthetically. I'm mainly looking to have a Wordpress version of this website that I built, away from the WIX ecosystem.
Updates

Need extra days to review

Target Market(s)

Psychology services clients

Coding

Coded - Design and coding required

Number of Pages Required

5+ page

Font styles to use
Serif

Requirements
Must have
• The finished product shoud match my website exactly.
Nice to have
• I'm happy to see new ideas that improve on the current website.
Should not have
• It should not be a different version of my website.

```html
<!DOCTYPE html>
<html lang="en">
<head>
<meta charset="utf-8">
<title>Linwell Psychology</title>
<link rel="stylesheet" href="https://fonts.googleapis.com/css2?family=Playfair+Display:wght@400;500;600&family=Source+Sans+3:wght@400;600&display=swap">
<style>
:root{
  --green:#2e5a4f;
  --green-line:#3f7a68;
  --white:#ffffff;
  --ink:#1f2a27;
}
*{margin:0;padding:0;box-sizing:border-box}
html,body{width:1200px;height:3700px;overflow:hidden;background:var(--white)}
body{font-family:"Source Sans 3",sans-serif;color:var(--ink);position:relative}
a{color:inherit}

/* header */
.site-header{position:absolute;top:0;left:0;width:1200px;height:89px;background:var(--white)}
.brand{position:absolute;left:52px;top:30px;display:flex;align-items:center;gap:10px;font-family:"Playfair Display",serif;font-size:22px;color:var(--green)}
.brand-dot{width:12px;height:12px;border-radius:50%;background:var(--green)}
.main-nav{position:absolute;top:35px;left:684px;font-family:"Playfair Display",serif;font-size:15px;color:#333}
.main-nav span{position:absolute;white-space:nowrap}

/* hero */
.hero{position:absolute;top:89px;left:0;width:1200px;height:765px;border-left:1px solid var(--green);overflow:hidden}
.hero-art{position:absolute;left:0;top:0}
.hero h1{position:absolute;left:86px;top:168px;font-family:"Playfair Display",serif;font-weight:600;font-size:46px;color:var(--green)}
.hero .roles{position:absolute;left:86px;top:233px;font-size:14.5px;line-height:22px;color:#222}
.divider{display:block;height:1px;background:currentColor;width:64px}
.hero .divider{position:absolute;left:86px;top:306px;color:var(--green-line)}
.hero .intro{position:absolute;left:86px;top:336px;width:430px;font-size:20.5px;line-height:30px;color:#222}
.btn{position:absolute;display:flex;align-items:center;justify-content:center;border-radius:22px;font-size:15px;letter-spacing:2.2px;font-weight:600}
.btn-solid{background:var(--green);color:var(--white);box-shadow:0 3px 6px rgba(0,0,0,.25)}
.btn-outline{border:1px solid var(--green);color:var(--green);background:var(--white);box-shadow:0 2px 4px rgba(0,0,0,.15)}
.btn-light{background:var(--white);color:var(--green)}

/* about */
.about{position:absolute;top:854px;left:0;width:1200px;height:656px;background:var(--green);color:var(--white);overflow:hidden}
.section-title{position:absolute;width:100%;text-align:center;font-family:"Playfair Display",serif;font-weight:400;font-size:44px;color:var(--white)}
.about .section-title{top:94px}
.about .divider,.psych .divider{position:absolute;left:552px;width:96px;color:#6fa08e}
.about .divider{top:172px}
.about-col{position:absolute;top:236px;width:510px;font-size:14.2px;line-height:22.5px}
.about-col p+p{margin-top:22.5px}
.about-col.left{left:53px}
.about-col.right{left:642px;width:500px}

/* focus tiles */
.focus{position:absolute;top:1510px;left:0;width:1200px;height:439px;display:flex}
.tile{position:relative;width:400px;height:439px;display:flex;align-items:center;justify-content:center}
.tile h3{position:relative;font-family:"Playfair Display",serif;font-weight:400;font-size:25px;color:var(--white);white-space:nowrap}
.tile-1{background:linear-gradient(135deg,#8f8f98,#74768a 60%,#6b6d7a)}
.tile-2{background:linear-gradient(135deg,#8a7b7c,#6f6a78 55%,#4c4650)}
.tile-3{background:linear-gradient(135deg,#7a6a6a,#6a5c60 55%,#5a4d50)}

/* psychosexual */
.psych{position:absolute;top:1949px;left:0;width:1200px;height:525px;background:var(--green);color:var(--white);overflow:hidden}
.psych .section-title{top:96px}
.psych .divider{top:175px}
.psych .lead{position:absolute;top:237px;left:180px;width:840px;text-align:center;font-size:14.2px;line-height:22.5px}
.psych .ask{position:absolute;top:340px;width:100%;text-align:center;font-size:14.2px}

/* services */
.services{position:absolute;top:2474px;left:0;width:1200px;height:478px;background:var(--white)}
.service{position:absolute;top:104px;width:330px;text-align:center}
.service h3{font-family:"Playfair Display",serif;font-weight:500;font-size:28px;line-height:36px;color:var(--green)}
.service .divider{margin:22px auto 0;color:var(--green-line)}
.service p{margin-top:26px;font-size:14.2px;line-height:22.5px;color:#222;text-align:left;padding:0 8px}

/* footer */
.site-footer{position:absolute;top:2952px;left:0;width:1200px;height:748px;background:var(--green);color:var(--white);text-align:center;overflow:hidden}
.footer-brand{position:absolute;top:88px;left:0;width:100%;display:flex;justify-content:center;align-items:center;gap:12px;font-family:"Playfair Display",serif;font-size:28px}
.footer-brand .brand-dot{background:var(--white)}
.hours{position:absolute;top:170px;width:100%;font-size:14px;line-height:22.5px}
.support{position:absolute;top:294px;width:100%;font-size:14px;line-height:22.5px}
.lines{position:absolute;top:384px;width:100%;font-size:14px;line-height:22.5px}
.lines a{text-decoration:underline}
.social{position:absolute;top:627px;left:563px;display:flex;gap:12px}
.social span{width:16px;height:16px;border-radius:50%;background:var(--white)}
.rights{position:absolute;top:715px;width:100%;font-size:11px}
</style>
</head>
<body>

<header class="site-header">
  <div class="brand"><span class="brand-dot"></span>Linwell Psychology</div>
  <nav class="main-nav">
    <span style="left:0">Home</span>
    <span style="left:68px">About</span>
    <span style="left:135px">Services</span>
    <span style="left:218px">FAQs</span>
    <span style="left:279px">Fees &amp; Rebates</span>
    <span style="left:408px">Contact</span>
  </nav>
</header>

<section class="hero">
  <svg class="hero-art" width="1200" height="765" viewBox="0 0 1200 765">
    <defs>
      <linearGradient id="portraitTone" x1="0" y1="0" x2="1" y2="1">
        <stop offset="0" stop-color="#e6dfd8"/>
        <stop offset=".45" stop-color="#b76a4a"/>
        <stop offset=".75" stop-color="#6a4c3c"/>
        <stop offset="1" stop-color="#3c3a3e"/>
      </linearGradient>
    </defs>
    <path d="M545 0 C500 70 495 160 540 240 C590 330 560 430 560 520 C560 620 600 700 640 765 L1200 765 L1200 0 Z" fill="#dcdcdc"/>
    <path d="M575 0 C530 70 525 160 570 240 C620 330 590 430 590 520 C590 620 630 700 670 765 L1200 765 L1200 0 Z" fill="url(#portraitTone)" role="img" aria-label="Portrait photo of the psychologist writing notes on a clipboard in an armchair"/>
  </svg>
  <h1>Dr Ellis Marlowe</h1>
  <p class="roles">Clinical and Counselling Psychologist,<br>Clinical Psychosexual Therapist</p>
  <span class="divider"></span>
  <p class="intro">I am a Clinical and Counselling Psychologist, and accredited Clinical Psychosexual Therapist, with over 15 years’ experience working with adults and young people of all abilities and identities</p>
  <a class="btn btn-solid" style="left:86px;top:511px;width:242px;height:42px">Book an Appointment</a>
  <a class="btn btn-outline" style="left:355px;top:511px;width:111px;height:42px">Contact</a>
</section>

<section class="about">
  <h2 class="section-title">About Me</h2>
  <span class="divider"></span>
  <div class="about-col left">
    <p>My name is Ellis (he/they) and I am a Clinical and Counselling Psychologist, and accredited Clinical Psychosexual Therapist, with over 15 years’ experience working with adults and young people of all abilities and identities.</p>
    <p>My practice focuses on sex therapy and working with diversity, which regularly includes supporting members of LGBTQIA+, neurodivergent, and disabled communities. Because of this work, I am sex-positive and kink-, polyamory-, LGBTQIA+ and neurodiversity knowledgeable and affirming in my practice. I am also a member of many lived experience communities as part of my commitment to lifelong learning and honoring lived experience.</p>
    <p>I know that seeing a therapist can sometimes be anxiety-evoking, and as such, I always aim to curate a non-judgmental, collaborative, and intentional approach to working with people toward their personal goals and a life of value.</p>
  </div>
  <div class="about-col right">
    <p>In my work, I balance supportive counselling with evidence-based therapies, such as: humanistic therapy, cognitive-behavioural therapy, acceptance and commitment therapy, compassion-focused therapy, and solution-focused counselling. My work is also underpinned by intersectional feminist and social justice frameworks. As part of ensuring that you are benefiting from your sessions, I will regularly check in to see if you’re finding your session helpful to ensure you feel understood, respected, and that your sessions are relevant and on track.</p>
    <p>In addition to my client work, I am also a board accredited CSTA supervisor and enjoy supporting and supervising the practice of other clinicians, both trainee and experienced. And enjoy consultancy and training work with practices and organisations.</p>
  </div>
</section>

<section class="focus">
  <div class="tile tile-1" role="img" aria-label="Photo of an older couple laughing together"><h3>Intimacy &amp; Connection</h3></div>
  <div class="tile tile-2" role="img" aria-label="Photo of a couple celebrating at a wedding"><h3>Neurodivergence &amp; Disability</h3></div>
  <div class="tile tile-3" role="img" aria-label="Close-up photo of two people resting together"><h3>Gender Identity &amp; Affirmation</h3></div>
</section>

<section class="psych">
  <h2 class="section-title">What is a Clinical Psychosexual Therapist?</h2>
  <span class="divider"></span>
  <p class="lead">Sometimes referred to as a sex therapist, a Clinical Psychosexual Therapist is someone who has postgraduate university qualifications in the field of human sexuality, which is a broad area encompassing subjects like: sexual orientation, gender identity, sexual function and diversity, sexual and reproductive health, intersectional feminism, relationship dynamics, and sexual trauma.</p>
  <p class="ask">| How can a clinical psychosexual therapist help me? |</p>
  <a class="btn btn-light" style="left:535px;top:386px;width:132px;height:40px">Learn More</a>
</section>

<section class="services">
  <div class="service" style="left:55px">
    <h3>Psychological<br>Therapy</h3>
    <span class="divider"></span>
    <p>Psychological assessment, education, counselling, and therapy using person-centered and evidence-based integrative therapeutic interventions.</p>
  </div>
  <div class="service" style="left:435px">
    <h3>Clinical<br>Supervision</h3>
    <span class="divider"></span>
    <p>Psychological assessment, education, counselling, and therapy using person-centered and evidence-based integrative therapeutic interventions.</p>
  </div>
  <div class="service" style="left:811px">
    <h3>Training and<br>Consultancy</h3>
    <span class="divider"></span>
    <p>Psychological assessment, education, counselling, and therapy using person-centered and evidence-based integrative therapeutic interventions.</p>
  </div>
  <a class="btn btn-outline" style="left:152px;top:311px;width:143px;height:40px">Learn more</a>
  <a class="btn btn-outline" style="left:528px;top:311px;width:143px;height:40px">Learn more</a>
  <a class="btn btn-outline" style="left:904px;top:311px;width:143px;height:40px">Learn more</a>
</section>

<footer class="site-footer">
  <div class="footer-brand"><span class="brand-dot"></span>Linwell Psychology</div>
  <p class="hours"><strong>Practice Hours<br>(by appointment only):</strong><br>Mondays 9:30am - 3:30pm<br>Thursdays: 8:30am - 2:30pm</p>
  <p class="support"><strong>If you need support between<br>appointments or after hours,<br>please consider contacting:</strong></p>
  <p class="lines">
    <a>Brightline</a> on 13 40 21<br>
    <a>Young Voices Line</a> on 1800 300 412<br>
    <a>Harbour Men's Line</a> on 1300 510 736<br>
    <a>Safe Return Call Service</a> on 1300 482 905<br>
    <a>Clearsky Support</a> on 1300 61 72 48<br>
    <a>Youthroom</a> on 1800 274 316<br>
    <a>Spectrum Line</a> on 1800 392 604<br>
    <a>Yarning Circle Line</a> on 13 58 20
  </p>
  <div class="social" aria-label="Social media links"><span></span><span></span><span></span></div>
  <p class="rights">All Right Reserved</p>
</footer>

</body>
</html>
```